Business Card Design for Event Planning Company

Create a business card for event planning company using our new logo. After I pick the design, I will need files made for 6 employees. Our company provides event design & logistics services as well as venue management. The font should be sans serif and complementary to the logo. I will need to know the name of the font selected for the final design. The phone numbers listed should be separated by "." not "-"

Address for the card
PO Box 318, Washington, DC 20019

Card One
Lorna Pettibone
lpettibone@galavoyant.com
202.481.7730

Card Two
Miriam Okonkwo
mokonkwo@galavoyant.com
202.556.2047

Card Three
Tessa Varnholt
tvarnholt@galavoyant.com
978.620.4471

Card Four
Robin Fess
rfess@galavoyant.com
202.718.3362

Card Five
Ada-Rose Pelletan-Uzor
adarose@galavoyant.com
202.839.1205

Card Six
Beatrix Holloway
Beatrix@galavoyant.com
202.492.6618

Target Market(s)

Corporate/Non-Profit

Industry/Entity Type

Event Planning

Contact Information for Business Card

Address for the card

Card One
Lorna Pettibone
lpettibone@galavoyant.com
202.481.7730

Card Two
Miriam Okonkwo
202.556.2047

Card Three
Tessa Varnholt
978.620.4471

Card Four
Robin Fess
rfess@galavoyant.com
202.718.3362

Card Five
Ada-Rose Pelletan-Uzor
202.839.1205

Card Six
Beatrix Holloway
202.492.6618

Font styles to use
Sans Serif

Colors

Designer to choose colors to be used in the design.

Requirements
Must have
• Two-sided with logo
Should not have
• Extra colors or be too busy

```html
<!DOCTYPE html>
<html lang="en">
<head>
<meta charset="utf-8">
<title>Galavoyant Business Card</title>
<link rel="stylesheet" href="https://fonts.googleapis.com/css2?family=Mulish:wght@400;700&family=Questrial&display=swap">
<style>
  :root {
    --teal: #5ba5a5;
    --teal-text: #5aa3a3;
    --card-light: #eff0f0;
    --card-edge: #d9dada;
    --divider: #a3a4a4;
    --ink: #5a5b5c;
    --icon: #7d7e80;
    --white: #ffffff;
    --page: #ffffff;
  }
  * { box-sizing: border-box; margin: 0; padding: 0; }
  html, body {
    width: 1200px;
    height: 366px;
    overflow: hidden;
    background: var(--page);
  }
  .canvas {
    position: relative;
    width: 1200px;
    height: 366px;
  }
  .card {
    position: absolute;
    top: 0;
    width: 580px;
    height: 366px;
  }
  .card--front {
    left: 0;
    background: radial-gradient(ellipse 70% 110% at 48% 40%, var(--card-light) 0%, #e9eaea 45%, var(--card-edge) 100%);
  }
  .card--back {
    left: 620px;
    background: var(--teal);
  }
  .wordmark {
    position: absolute;
    font-family: "Questrial", "Mulish", sans-serif;
    font-weight: 400;
    white-space: nowrap;
    line-height: 1;
  }
  .card--front .wordmark {
    left: 158px;
    top: 186px;
    transform: translateX(-50%);
    font-size: 28px;
    color: var(--teal-text);
  }
  .card--back .wordmark {
    left: 50%;
    top: 188px;
    transform: translateX(-50%);
    font-size: 46px;
    color: var(--white);
  }
  .divider {
    position: absolute;
    left: 268px;
    top: 84px;
    width: 2px;
    height: 197px;
    background: var(--divider);
  }
  .contact {
    position: absolute;
    left: 284px;
    top: 98px;
    font-family: "Mulish", sans-serif;
    color: var(--ink);
  }
  .contact__name {
    font-size: 18px;
    letter-spacing: 0.4px;
    color: var(--teal-text);
    font-weight: 400;
    text-transform: uppercase;
    margin-bottom: 33px;
  }
  .contact__name strong { font-weight: 700; }
  .contact__list { list-style: none; }
  .contact__item {
    display: flex;
    align-items: flex-start;
    font-size: 14px;
    line-height: 18px;
    margin-bottom: 17px;
  }
  .contact__icon {
    flex: 0 0 16px;
    width: 16px;
    height: 18px;
    margin-right: 14px;
    stroke: var(--icon);
    fill: none;
    stroke-width: 1.1;
  }
</style>
</head>
<body>
<main class="canvas">
  <section class="card card--front" aria-label="Card front">
    <div class="wordmark">galavoyant</div>
    <div class="divider"></div>
    <div class="contact">
      <h1 class="contact__name"><strong>Lorna</strong> Pettibone</h1>
      <ul class="contact__list">
        <li class="contact__item">
          <svg class="contact__icon" viewBox="0 0 16 18" aria-hidden="true">
            <rect x="0.8" y="4.5" width="14.4" height="10" />
            <polyline points="0.8,4.5 8,10.5 15.2,4.5" />
            <line x1="0.8" y1="14.5" x2="6" y2="9.3" />
            <line x1="15.2" y1="14.5" x2="10" y2="9.3" />
          </svg>
          <span>lpettibone@galavoyant.com</span>
        </li>
        <li class="contact__item">
          <svg class="contact__icon" viewBox="0 0 16 18" aria-hidden="true">
            <rect x="3.5" y="0.8" width="9" height="16.4" rx="1.2" />
            <line x1="3.5" y1="3.5" x2="12.5" y2="3.5" />
            <line x1="3.5" y1="13.5" x2="12.5" y2="13.5" />
            <circle cx="8" cy="15.4" r="0.7" />
          </svg>
          <span>202.481.7730</span>
        </li>
        <li class="contact__item">
          <svg class="contact__icon" viewBox="0 0 16 18" aria-hidden="true">
            <path d="M8 16.8 C4.5 12 2.5 9 2.5 6.3 A5.5 5.5 0 0 1 13.5 6.3 C13.5 9 11.5 12 8 16.8 Z" />
            <circle cx="8" cy="6.3" r="2" />
          </svg>
          <span>PO Box 318,<br>Washington, DC 20019</span>
        </li>
      </ul>
    </div>
  </section>

  <section class="card card--back" aria-label="Card back">
    <div class="wordmark">galavoyant</div>
  </section>
</main>
</body>
</html>
```